Titleway Conveyancing Group

We are a legal service provider.
We deal predominately with Real Estate title transfers.
We will be printing on white paper with black ink, so colour is not really needed for the letter head.

I have enclosed our logo which i will like to be incorporated into the letterhead.

I have also attached a copy of our current old letterhead with all our office details on there. Everything that is listed in the current letterhead i would like to be included in the new one.

Target Market(s)

Real Estate, Home buyers & Sellers, Solicitors and Lawyers, Pest & Building Inspectors

Industry/Entity Type

Legal

Font styles to use
Serif

Requirements
Must have
• Simple and Legal looking.

```html
<!DOCTYPE html>
<html lang="en">
<head>
<meta charset="utf-8">
<title>Titleway Conveyancing Group — Letterhead</title>
<link rel="stylesheet" href="https://fonts.googleapis.com/css2?family=Libre+Baskerville:wght@400;700&display=swap">
<style>
  :root {
    --paper: #ffffff;
    --brand-red: #b3262c;
    --ink-grey: #5a5a5a;
    --card-edge: #8a8a8a;
  }
  * { margin: 0; padding: 0; box-sizing: border-box; }
  html, body { width: 851px; height: 1200px; overflow: hidden; background: var(--paper); }
  body { font-family: "Libre Baskerville", Georgia, serif; position: relative; }

  .letterhead { position: absolute; inset: 0; background: var(--paper); }

  .brand {
    position: absolute;
    display: flex;
    align-items: center;
    gap: 12px;
    color: var(--brand-red);
    font-weight: 700;
  }
  .brand-mark { background: var(--brand-red); flex: none; }
  .brand-name { line-height: 1.05; letter-spacing: 0.04em; }
  .brand-name span { display: block; }

  .letterhead-brand { top: 48px; left: 440px; }
  .letterhead-brand .brand-mark { width: 44px; height: 44px; }
  .letterhead-brand .brand-name { font-size: 40px; }
  .letterhead-brand .brand-name .line-two { font-size: 17.5px; letter-spacing: 0.06em; margin-top: 4px; }

  .office-details {
    position: absolute;
    top: 156px;
    right: 66px;
    text-align: right;
    color: var(--brand-red);
    font-weight: 700;
    font-size: 13.5px;
    line-height: 1.55;
    list-style: none;
  }
  .office-details .phone { color: var(--ink-grey); font-weight: 400; letter-spacing: 0.06em; }

  .business-card {
    position: absolute;
    top: 558px;
    left: 430px;
    width: 358px;
    height: 202px;
    border: 1px solid var(--card-edge);
    background: var(--paper);
  }
  .card-brand { top: 22px; left: 88px; gap: 8px; }
  .card-brand .brand-mark { width: 26px; height: 26px; }
  .card-brand .brand-name { font-size: 23px; }
  .card-brand .brand-name .line-two { font-size: 10px; letter-spacing: 0.06em; margin-top: 3px; }

  .card-holder {
    position: absolute;
    top: 126px;
    left: 36px;
    color: var(--brand-red);
    font-weight: 700;
    font-size: 11px;
    letter-spacing: 0.05em;
  }
  .card-details {
    position: absolute;
    top: 92px;
    right: 12px;
    text-align: right;
    list-style: none;
    font-size: 10px;
    line-height: 1.5;
    color: #333;
  }
  .card-details .phone { color: var(--ink-grey); letter-spacing: 0.06em; }
</style>
</head>
<body>
<main class="letterhead">
  <header class="brand letterhead-brand">
    <div class="brand-mark"></div>
    <div class="brand-name">
      <span class="line-one">TITLEWAY</span>
      <span class="line-two">CONVEYANCING GROUP</span>
    </div>
  </header>

  <ul class="office-details">
    <li>Address Line One</li>
    <li>Address Line Two</li>
    <li>City State 000000</li>
    <li>webaddress.com</li>
    <li class="phone">000-000-0000</li>
  </ul>

  <section class="business-card">
    <div class="brand card-brand">
      <div class="brand-mark"></div>
      <div class="brand-name">
        <span class="line-one">TITLEWAY</span>
        <span class="line-two">CONVEYANCING GROUP</span>
      </div>
    </div>
    <p class="card-holder">FIRST LAST NAME</p>
    <ul class="card-details">
      <li>Address Line One</li>
      <li>Address Line Two</li>
      <li>City State 000000</li>
      <li>email@web.com</li>
      <li>webaddress.com</li>
      <li class="phone">000-000-0000</li>
    </ul>
  </section>
</main>
</body>
</html>
```